Coffee label for coffee brand - Kiln Lantern coffee

We want someone to design a label for packaging of a coffee line. The design will then be printed on stickers.

It is called Kiln Lantern Coffee (logo enclosed) I want to incorporate a streetscape and the idea is that with every different coffee it will be a different colour (we have 6 varieties at the moment) with a black background. It needs to have a modern feel.

It needs to have a blank area towards the bottom for the type of coffee which we will print later on)

text to include

'Roasting exceptional coffee'

Target Market(s)

Coffee drinkers - modern feel

Font styles to use
Sans Serif

Colors
f78f20
9bcb3b
33a6d7
b768aa

Requirements
Must have
• the logo incorporated
• Space for coffee variety
• Quote' Roasting exceptional coffee'
Nice to have
• Streetscape theme incorporated - bright colour varieties (would love metallic) (on black background)

```html
<!DOCTYPE html>
<html lang="en">
<head>
<meta charset="utf-8">
<title>Kiln Lantern Coffee – Labels</title>
<link href="https://fonts.googleapis.com/css2?family=Roboto+Condensed:wght@300;400;700&display=swap" rel="stylesheet">
<style>
  :root {
    --bg: #dcdfe0;
    --ink: #000000;
    --paper: #ffffff;
    --blue: #1ea3dc;
    --blue-deep: #0b4d72;
    --blue-line: #0c5f88;
    --orange: #f5952a;
    --orange-deep: #b2521a;
    --orange-line: #a9551b;
    --amber: #f2c21f;
  }
  * { box-sizing: border-box; margin: 0; padding: 0; }
  html, body { width: 1200px; height: 900px; overflow: hidden; }
  body {
    background: var(--bg);
    font-family: "Roboto Condensed", Arial, sans-serif;
    position: relative;
  }
  .label-row {
    position: absolute;
    top: 172px; left: 135px;
    display: flex; gap: 70px;
  }
  .label {
    position: relative;
    width: 430px; height: 557px;
    background: var(--ink);
    overflow: hidden;
  }
  .label--ethiopia { --accent: var(--blue); --accent-deep: var(--blue-deep); --rule: var(--blue-line); }
  .label--brazil   { --accent: var(--orange); --accent-deep: var(--orange-deep); --rule: var(--orange-line); }

  .streetscape {
    position: absolute; left: 0; top: 0;
    width: 100%; height: 420px;
  }
  .label--ethiopia .streetscape {
    background:
      linear-gradient(180deg, rgba(0,0,0,0.9) 0%, rgba(0,0,0,0.2) 55%, rgba(0,0,0,0) 100%),
      linear-gradient(90deg, #0a3e5c 0%, #000 35%, #071f30 60%, #0a3e5c 100%);
  }
  .label--brazil .streetscape {
    background:
      linear-gradient(90deg, #d7a21c 0%, #5a3b0a 25%, #e98a2f 45%, #d97a30 55%, #1a1003 75%, #000 100%);
  }

  .crest {
    position: absolute; left: 118px; top: 0;
    width: 194px; height: 202px;
  }
  .brand-name {
    position: absolute; left: 118px; top: 60px;
    width: 194px;
    text-align: center;
    color: var(--paper);
    font-weight: 700;
    font-size: 27px;
    line-height: 1.05;
    text-transform: uppercase;
  }

  .tagline {
    position: absolute; left: 0; top: 298px;
    width: 134px; height: 70px;
  }
  .tagline-text {
    position: absolute; left: 16px; top: 306px;
    font-size: 12px; font-weight: 700; line-height: 1.15;
    color: #10171c; text-transform: uppercase;
  }

  .info-band {
    position: absolute; left: 0; top: 420px;
    width: 100%; height: 137px;
    background: var(--accent);
    border-top: 3px solid var(--accent-deep);
    color: #101010;
  }
  .info-main {
    position: absolute; left: 0; top: 0;
    width: 268px; height: 100%;
    border-right: 2px solid var(--rule);
    text-align: center;
  }
  .variety {
    margin-top: 8px;
    font-size: 38px; font-weight: 700; letter-spacing: 0.5px;
  }
  .variety-form { font-size: 10px; font-weight: 400; margin-top: -2px; text-transform: uppercase; }
  .strength {
    position: absolute; left: 0; top: 74px; width: 100%;
    font-size: 10px; font-weight: 700; text-transform: uppercase;
  }
  .strength-dots { display: inline-flex; gap: 2px; vertical-align: -1px; margin-left: 4px; }
  .dot { width: 8px; height: 8px; border-radius: 50%; border: 1.5px solid #101010; }
  .dot--on { background: #101010; }
  .website {
    position: absolute; left: 0; top: 103px; width: 100%;
    border-top: 2px solid var(--rule);
    padding-top: 8px;
    font-size: 10px; font-weight: 700;
  }
  .info-side { position: absolute; left: 270px; top: 0; width: 160px; height: 100%; }
  .weight { margin: 6px 0 0 12px; font-size: 44px; font-weight: 300; line-height: 1; }
  .weight-label { margin-left: 14px; font-size: 9px; font-weight: 700; text-transform: uppercase; }
  .detail-row {
    position: absolute; left: 0; width: 100%;
    border-top: 2px solid var(--rule);
    padding: 6px 0 0 14px;
    font-size: 10px; font-weight: 700; text-transform: uppercase;
  }
  .detail-row--roasted { top: 78px; }
  .detail-row--expiry { top: 103px; }
</style>
</head>
<body>
  <main class="label-row">
    <article class="label label--ethiopia">
      <div class="streetscape" role="img" aria-label="Blue city streetscape illustration on black, skyscrapers lining a street"></div>
      <svg class="crest" viewBox="0 0 194 202" aria-hidden="true">
        <polygon points="0,0 194,0 194,138 97,202 0,138" fill="rgba(0,0,0,0.82)" stroke="#1ea3dc" stroke-width="1"/>
      </svg>
      <div class="brand-name">Kiln Lantern<br>Coffee</div>
      <svg class="tagline" viewBox="0 0 134 70" aria-hidden="true">
        <defs>
          <linearGradient id="tag-blue" x1="0" x2="1">
            <stop offset="0" stop-color="#1ea3dc"/>
            <stop offset="1" stop-color="#5cc4ef"/>
          </linearGradient>
        </defs>
        <polygon points="0,0 106,0 134,35 106,70 0,70" fill="url(#tag-blue)"/>
      </svg>
      <p class="tagline-text">Roasting<br>exceptional<br>coffee</p>
      <section class="info-band">
        <div class="info-main">
          <h2 class="variety">ETHIOPIA</h2>
          <p class="variety-form">Whole beans</p>
          <p class="strength">Strength:
            <span class="strength-dots"><i class="dot dot--on"></i><i class="dot dot--on"></i><i class="dot dot--on"></i><i class="dot"></i><i class="dot"></i></span>
          </p>
          <p class="website">www.kilnlanterncoffee.com</p>
        </div>
        <div class="info-side">
          <p class="weight">500g</p>
          <p class="weight-label">Net wt.</p>
          <p class="detail-row detail-row--roasted">Roasted in:</p>
          <p class="detail-row detail-row--expiry">Expiry date:</p>
        </div>
      </section>
    </article>

    <article class="label label--brazil">
      <div class="streetscape" role="img" aria-label="Orange and amber city streetscape illustration on black, skyscrapers lining a street"></div>
      <svg class="crest" viewBox="0 0 194 202" aria-hidden="true">
        <polygon points="0,0 194,0 194,138 97,202 0,138" fill="rgba(214,110,40,0.55)"/>
      </svg>
      <div class="brand-name">Kiln Lantern<br>Coffee</div>
      <svg class="tagline" viewBox="0 0 134 70" aria-hidden="true">
        <defs>
          <linearGradient id="tag-orange" x1="0" x2="1">
            <stop offset="0" stop-color="#f2c21f"/>
            <stop offset="1" stop-color="#e2683a"/>
          </linearGradient>
        </defs>
        <polygon points="0,0 106,0 134,35 106,70 0,70" fill="url(#tag-orange)"/>
      </svg>
      <p class="tagline-text">Roasting<br>exceptional<br>coffee</p>
      <section class="info-band">
        <div class="info-main">
          <h2 class="variety">BRAZIL</h2>
          <p class="variety-form">Whole beans</p>
          <p class="strength">Strength:
            <span class="strength-dots"><i class="dot dot--on"></i><i class="dot dot--on"></i><i class="dot dot--on"></i><i class="dot dot--on"></i><i class="dot"></i></span>
          </p>
          <p class="website">www.kilnlanterncoffee.com</p>
        </div>
        <div class="info-side">
          <p class="weight">500g</p>
          <p class="weight-label">Net wt.</p>
          <p class="detail-row detail-row--roasted">Roasted in:</p>
          <p class="detail-row detail-row--expiry">Expiry date:</p>
        </div>
      </section>
    </article>
  </main>
</body>
</html>
```